Modern Design Business Card industrial maintenance company

Business card design for Company named Brookvale Equipment Services

Target Market(s)

Industrial

Industry/Entity Type

Maintenance and repair

Contact Information for Business Card

Place holder for address, office phone, mobile number and email

Requirements
Must have
• Clean modern look
Nice to have
• N/a

```html
<!DOCTYPE html>
<html lang="en">
<head>
<meta charset="utf-8">
<title>Brookvale Equipment Services – Business Card</title>
<link rel="stylesheet" href="https://fonts.googleapis.com/css2?family=Archivo:wght@600;700&family=Open+Sans:wght@400;600&display=swap">
<style>
  :root {
    --bg: #2c2c2d;
    --card-dark: #1b1b1c;
    --card-light: #ffffff;
    --ink: #111111;
    --silver: #c7c7c9;
    --ghost: #e4e3e6;
    --rule: #3a3a3a;
  }
  * { margin: 0; padding: 0; box-sizing: border-box; }
  html, body { width: 1200px; height: 895px; overflow: hidden; }
  body {
    background: var(--bg);
    position: relative;
    font-family: "Open Sans", sans-serif;
    color: var(--ink);
  }
  .card {
    position: absolute;
    top: 299px;
    width: 520px;
    height: 297px;
    border-radius: 18px;
    overflow: hidden;
    box-shadow: 0 12px 30px rgba(0,0,0,.45);
  }
  /* Front */
  .card-front { left: 45px; background: var(--card-dark); }
  .front-lockup {
    position: absolute; inset: 0;
    display: flex; flex-direction: column; align-items: center; justify-content: center;
    gap: 14px;
  }
  .front-mark {
    width: 74px; height: 74px; border-radius: 50%;
    border: 3px solid var(--silver);
  }
  .front-name {
    font-family: "Archivo", sans-serif; font-weight: 600;
    color: var(--silver); text-align: center; text-transform: uppercase;
    line-height: 1.15;
  }
  .front-name .line-main { display: block; font-size: 30px; letter-spacing: 3px; }
  .front-name .line-sub { display: block; font-size: 11px; letter-spacing: 6px; }

  /* Back */
  .card-back { left: 635px; background: var(--card-light); }
  .ghost-ring {
    position: absolute; right: 14px; top: -40px;
    width: 250px; height: 250px; border-radius: 50%;
    border: 12px solid var(--ghost);
  }
  .brand {
    position: absolute; left: 30px; top: 32px;
    display: flex; align-items: center; gap: 10px;
  }
  .brand-mark { width: 46px; height: 46px; border-radius: 50%; border: 3px solid var(--ink); flex: none; }
  .brand-name {
    font-family: "Archivo", sans-serif; font-weight: 700;
    font-size: 17px; letter-spacing: 1.5px; text-transform: uppercase; line-height: 1.1;
    color: var(--ink);
  }
  .brand-name span { display: block; }
  .brand-name .brand-sub { font-size: 8.5px; letter-spacing: 3.3px; }

  .person { position: absolute; left: 30px; top: 140px; }
  .person-name { font-family: "Archivo", sans-serif; font-weight: 700; font-size: 22px; line-height: 1.2; }
  .person-title { font-size: 16px; line-height: 1.3; }

  .rule-thick { position: absolute; left: 30px; top: 208px; width: 165px; height: 3px; background: var(--ink); }
  .rule-thin { position: absolute; left: 195px; top: 209px; width: 300px; height: 1px; background: var(--rule); }

  .contacts { position: absolute; left: 30px; top: 220px; list-style: none; font-size: 13px; line-height: 20px; }
  .contacts li { display: flex; align-items: center; gap: 7px; }
  .contacts svg { width: 12px; height: 12px; flex: none; }

  .address { position: absolute; right: 28px; top: 218px; text-align: right; font-size: 13px; line-height: 18px; }
  .address svg { width: 12px; height: 14px; display: block; margin: 0 0 2px auto; }
</style>
</head>
<body>

<section class="card card-front" aria-label="Card front">
  <div class="front-lockup">
    <div class="front-mark"></div>
    <div class="front-name">
      <span class="line-main">Brookvale</span>
      <span class="line-sub">Equipment Services</span>
    </div>
  </div>
</section>

<section class="card card-back" aria-label="Card back">
  <div class="ghost-ring"></div>

  <div class="brand">
    <div class="brand-mark"></div>
    <div class="brand-name">
      <span>Brookvale</span>
      <span class="brand-sub">Equipment Services</span>
    </div>
  </div>

  <div class="person">
    <p class="person-name">Daniel Hargrove</p>
    <p class="person-title">Founder &amp; CEO</p>
  </div>

  <div class="rule-thick"></div>
  <div class="rule-thin"></div>

  <ul class="contacts">
    <li>
      <svg viewBox="0 0 12 12" fill="none" stroke="#333" stroke-width="1"><path d="M2 1.5l2 0 1 2.5-1.3 1a6 6 0 0 0 3.3 3.3l1-1.3 2.5 1v2a1 1 0 0 1-1 1A9 9 0 0 1 1 2.5a1 1 0 0 1 1-1z"/></svg>
      (555)-010-0000
    </li>
    <li>
      <svg viewBox="0 0 12 12" fill="none" stroke="#333" stroke-width="1"><rect x="3" y="0.5" width="6" height="11" rx="1"/><line x1="5" y1="9.5" x2="7" y2="9.5"/></svg>
      (555)-010-0000
    </li>
    <li>
      <svg viewBox="0 0 12 12" fill="none" stroke="#333" stroke-width="1"><rect x="0.5" y="2.5" width="11" height="7"/><path d="M0.5 2.5l5.5 4 5.5-4"/></svg>
      info@brookvale-equip.com.au
    </li>
  </ul>

  <address class="address" style="font-style:normal">
    <svg viewBox="0 0 12 14" fill="none" stroke="#333" stroke-width="1"><path d="M6 13s-5-5-5-8a5 5 0 0 1 10 0c0 3-5 8-5 8z"/><circle cx="6" cy="5" r="1.8"/></svg>
    24 Quarry Lane, Ridgefield<br>SA 2041
  </address>
</section>

</body>
</html>
```